Dashboard Elements

Hello – looking for someone to create dashboard elements.
I’ve already basically designed all these elements – but I need someone to take what I’ve designed and make it look like an actual dashboard UI, like an app - assuming using some kind of dashboard UI kit (but however you would like to get it done is fine). It can look just like mine or try something different, as long as it matches the color scheme webpage that I’m going to out it on – see the page here. I’m ok with making it dark, maybe that would look better – again as long as it matches the webpage (https://www.plandeck.io/file/7KqWmb2TxRpLnVc4Hd8Fs3/Webpage-with-placeholders?node-id=0%3A1). Please note, you do not need to put anything on the webpage or do anything with this Figma file, this is just a reference so you can color/stylize it accordingly.

The attached Powerpoint file has everything you need - make sure to zoom all the way out to see everything on the slides.

Here are the Dashboard elements needed (this will all make sense when you look at the PPT):
Dashboard 1
Dashboard 1 – expanded view A
Dashboard 1 – expanded view B
View Source button by itself
Source Document Viewer 1 and 2 (these are exactly the same just with a different image inside)*
Dashboard 2 (only slightly different than Dashboard 1, just extended with extra headings
Table of Contents
Searchbar and Source Doc by itself
*the documents in the source document viewers should still look like documents - they don’t need to look like part of the UI, because this is a document viewer – you can restyle/recolor if necessary or just leave these as is.
- Colors must match color scheme of webpage, attached and on Figma link (images there currently are only placeholders) – ok to go dark as long as it matches
- Must look sleek, clean, realistic
- Don’t add any pictures of people or change the text.
- In case it’s not clear, this is what I mean by the concept of Dashboard UI - https://www.quillbin.com/shard/s7/sh/8c1d2fa0-42b7-9a3e-7d5c-03b8e1f9a6d4/71c4e2a09b3f6d58e2a1c7f04b9d3e62
- Must be sent in an editable file, I may need to be edit text and other elements
- If you are going to send a sample, please make sure it’s part of the dashboard itself, not just the table of contents etc

Ideally hoping to find someone I can continue working with as I'll have a lot more graphic design work needed coming up.

Thank you!

```html
<!DOCTYPE html>
<html lang="en">
<head>
<meta charset="utf-8">
<title>C-CDA Compendium – Dashboard Elements</title>
<link href="https://fonts.googleapis.com/css2?family=Barlow:wght@400;500;600&family=Barlow+Condensed:wght@500;600&display=swap" rel="stylesheet">
<style>
:root{
  --bg:#0b0f2b;
  --bg-deep:#080b22;
  --teal:#19c2d0;
  --teal-soft:#3fe0e6;
  --violet:#6a4cd8;
  --indigo:#3f4fd0;
  --card-top:#4657d6;
  --card-bot:#5a43c4;
  --row:#3947b8;
  --row-alt:#4350c6;
  --ink:#eef0ff;
  --ink-dim:#a9b0dd;
  --ink-faint:#6d75a8;
  --line:#3c4a8c;
  --panel:#12173a;
}
*{box-sizing:border-box;margin:0;padding:0}
html,body{width:769px;height:1200px;overflow:hidden}
body{
  position:relative;
  background:
    radial-gradient(circle at 20% 6%, rgba(80,60,200,.35), transparent 28%),
    radial-gradient(circle at 90% 22%, rgba(25,194,208,.18), transparent 25%),
    radial-gradient(circle at 15% 58%, rgba(25,150,190,.22), transparent 30%),
    radial-gradient(circle at 80% 80%, rgba(20,140,150,.25), transparent 30%),
    radial-gradient(circle at 30% 92%, rgba(90,60,200,.2), transparent 30%),
    var(--bg);
  font-family:"Barlow",sans-serif;color:var(--ink);
}
.abs{position:absolute}

/* intro */
.intro{left:82px;top:122px;width:260px}
.eyebrow{font-family:"Barlow Condensed",sans-serif;font-weight:600;font-size:13px;letter-spacing:.08em;color:var(--ink)}
.intro p{margin-top:10px;font-size:10.5px;line-height:1.5;color:var(--ink-dim)}

.dot{border-radius:50%}
.dot-teal{left:428px;top:108px;width:24px;height:24px;background:var(--teal);box-shadow:0 0 18px var(--teal)}
.dot-blue{left:402px;top:174px;width:16px;height:16px;background:#2f7fe0;box-shadow:0 0 14px #2f7fe0}
.pill-ccda{left:462px;top:138px;width:62px;height:24px;border:1px solid var(--teal);border-radius:6px;background:rgba(25,194,208,.12);font-size:10px;color:var(--teal-soft);display:flex;align-items:center;justify-content:center}

/* table of contents */
.toc{left:566px;top:-4px;width:154px;padding:8px 8px 10px;border-radius:10px;background:linear-gradient(160deg,var(--card-top),var(--card-bot));box-shadow:0 10px 30px rgba(40,30,140,.5)}
.toc-head{font-size:9px;color:var(--ink-dim);padding:3px 6px 7px;display:flex;justify-content:space-between}
.toc ul{list-style:none}
.toc li{font-size:9.5px;padding:3px 8px;color:var(--ink);border-radius:4px;margin-bottom:2px}
.toc li.active{background:#fff;color:var(--indigo);font-weight:600}
.toc li::before{content:"";display:inline-block;width:5px;height:5px;border-radius:50%;background:var(--teal-soft);margin-right:6px;vertical-align:middle}

/* insights section */
.insights{left:56px;top:379px;width:656px;height:291px;border:1px solid rgba(120,130,200,.2);background:rgba(20,26,70,.35)}
.insights h2{margin-top:74px;text-align:center;font-family:"Barlow Condensed",sans-serif;font-weight:500;font-size:29px;line-height:1.1;letter-spacing:.04em}
.insights p{margin:14px auto 0;width:420px;text-align:center;font-size:10px;line-height:1.55;color:var(--ink-dim)}

/* dashboard card */
.card{border-radius:10px;background:linear-gradient(170deg,var(--card-top),var(--card-bot));box-shadow:0 14px 40px rgba(40,30,160,.55)}
.dash{left:225px;top:594px;width:360px;height:212px;padding:10px 12px}
.dash-title{font-size:12px;font-weight:600;display:flex;align-items:center;gap:8px}
.dash-title::before{content:"";width:10px;height:10px;border-radius:3px;background:var(--teal-soft)}
.dash-sub{margin-top:8px;display:flex;justify-content:space-between;font-size:9px;color:var(--ink-dim);border-bottom:1px solid rgba(255,255,255,.18);padding-bottom:5px}
.dash-sub b{color:var(--ink);font-weight:600}
.tbl{margin-top:6px;width:100%;border-collapse:collapse;font-size:8px}
.tbl th{text-align:left;font-weight:500;color:var(--ink-dim);padding:3px 6px;background:rgba(255,255,255,.08)}
.tbl td{padding:5px 6px;border-bottom:1px solid rgba(255,255,255,.1)}
.tbl td.num{text-align:right;color:var(--teal-soft)}
.btn{display:inline-flex;align-items:center;gap:4px;border-radius:4px;font-size:8px;padding:3px 7px;background:#2c39a8;border:1px solid rgba(255,255,255,.25);color:var(--ink)}
.src-btn{left:520px;top:784px;background:var(--teal);color:#0b1a3a;font-weight:600;box-shadow:0 0 12px rgba(25,194,208,.6)}

/* source viewer card */
.viewer{left:148px;top:870px;width:488px;height:256px;padding:10px 14px}
.viewer-head{display:flex;gap:10px;align-items:center;font-size:9px}
.viewer-head .score{margin-left:auto;background:rgba(255,255,255,.15);border-radius:4px;padding:2px 8px}
.viewer-note{font-size:7.5px;color:var(--ink-dim);margin-top:4px}
.vrow{display:flex;align-items:center;font-size:8.5px;padding:10px 8px;margin-top:8px;background:rgba(20,25,90,.35);border-radius:6px}
.vrow span:first-child{width:170px}
.vrow .tag{color:var(--ink-dim);width:130px}
.vrow .btn{margin-left:auto}

.popup{background:#1c2560;border:1px solid rgba(120,140,230,.4);border-radius:6px;box-shadow:0 10px 30px rgba(0,0,0,.5);font-size:8.5px;display:flex;align-items:center}
.pop-left{left:51px;top:968px;width:206px;height:44px;padding:0 10px;gap:16px}
.pop-left small{display:block;font-size:7px;color:var(--ink-dim)}
.pop-right{left:397px;top:1050px;width:294px;height:52px;padding:0 12px;gap:40px}
.pop-right small{display:block;font-size:7px;color:var(--ink-dim);line-height:1.4}
.pop-right .btn{margin-left:auto}

.ring{width:34px;height:34px;border-radius:50%;border:1px solid rgba(140,150,220,.45);background:rgba(20,26,70,.6)}
</style>
</head>
<body>

<svg class="abs" width="769" height="300" style="left:0;top:0">
  <path d="M440 120 Q470 150 493 150 L566 150" fill="none" stroke="#19c2d0" stroke-width="1.2" opacity=".8"/>
  <line x1="410" y1="182" x2="410" y2="250" stroke="#2f7fe0" stroke-width="1" opacity=".5"/>
</svg>

<div class="abs dot dot-teal"></div>
<div class="abs dot dot-blue"></div>
<div class="abs pill-ccda">C-CDA</div>

<section class="abs intro">
  <div class="eyebrow">COMPENDIUM C-CDA</div>
  <p>The normalized data is unified into the Compendium C-CDA. Enhanced composite longitudinal record in C-CDA format, the industry standard for all interoperability initiatives</p>
</section>

<nav class="abs toc">
  <div class="toc-head"><span>Table of Contents</span><span>▾</span></div>
  <ul>
    <li class="active">Encounter Header</li>
    <li>Problems</li>
    <li>Results</li>
    <li>Procedures</li>
    <li>Encounters</li>
    <li>Medications</li>
    <li>Vital Signs</li>
    <li>Immunizations</li>
    <li>Social History</li>
    <li>Family History</li>
    <li>Plan of Care</li>
  </ul>
</nav>

<section class="abs insights">
  <h2>SUMMARIZED AND LINKED<br>TO KEY INSIGHTS</h2>
  <p>Insights are presented in a concise summary with direct links to supporting evidence. HCC opportunities are abstracted and cross-linked directly to the original text in the underlying record for quick and easy reference.</p>
</section>

<div class="abs card dash">
  <div class="dash-title">C-CDA Compendium</div>
  <div class="dash-sub"><b>HCC Summary</b><span>Total: 5 conditions · Score 2.41</span></div>
  <table class="tbl">
    <tr><th>HCC</th><th>Condition</th><th>Weight</th><th></th></tr>
    <tr><td>111</td><td>Chronic obstructive pulmonary disease</td><td class="num">0.335</td><td>↗</td></tr>
    <tr><td>138</td><td>Chronic kidney disease, moderate stage 3</td><td class="num">0.069</td><td>↗</td></tr>
    <tr><td>59</td><td>Major depressive disorder, recurrent</td><td class="num">0.309</td><td>↗</td></tr>
    <tr><td>22</td><td>Morbid obesity</td><td class="num">0.250</td><td>↗</td></tr>
    <tr><td>18</td><td>Type 2 diabetes mellitus with diabetic neuropathy</td><td class="num">0.302</td><td>↗</td></tr>
  </table>
</div>
<div class="abs btn src-btn">Source Document</div>

<div class="abs card viewer">
  <div class="viewer-head"><b>C-CDA</b><span>Type 2 diabetes mellitus with diabetic neuropathy</span><span class="score">0.302</span></div>
  <div class="viewer-note">This condition was identified from the sections below in the source document.</div>
  <div class="vrow"><span>Nonhispanic Caucasian (race)</span><span class="tag">C-CDA: PROCEDURES</span><span class="btn">▣ View source</span></div>
  <div class="vrow"><span>Diabetes Type 2</span><span class="tag">C-CDA: PROBLEM LIST</span><span class="btn">▣ View source</span></div>
  <div class="vrow"><span>Diabetic neuropathy</span><span class="tag">C-CDA: RESULTS</span><span class="btn">▣ View source</span></div>
  <div class="vrow"><span>Established Drug User</span><span class="tag">C-CDA: PROBLEM LIST</span><span class="btn">▣ View source</span></div>
</div>

<div class="abs popup pop-left"><span>Subsection</span><span>Ophthalmology Visit note<small>Retinal exam shows signs of diabetic changes</small></span></div>
<div class="abs popup pop-right"><span>Status</span><span>Lab results<small>Hemoglobin A1C<br>8.1%<br>Elevated</small></span><span class="btn">▣ View source</span></div>

<div class="abs ring" style="left:91px;top:1170px"></div>
<div class="abs ring" style="left:643px;top:1141px"></div>

</body>
</html>
```